依頼詳細
資料請求に特化したいので、よくある縦に長いランディングページではなく、ぱっと見てとりあえず資料を請求したくなるようなページが希望です。
したがって、キャッチコピー(アイキャッチ)はファーストビュー(画面に見える形)で、縦は長くてもA4判の縦の比率でお願いします。
必ず入れてほしい項目は「補足説明」に記載の通りですが、その他のキャッチや文章などはお任せです。
資料請求したくなるような文面とデザインをご提案いただけましたら幸いです。
サイトURL
http://www.rovino.net/
ページ数
1ページ
希望イメージ
シンプル 複雑
単色 カラフル
暗い 明るい
日常 高級
遊び心 厳粛
未来的 伝統的
女性的 男性的
希望する色
色の指定はありませんが、明るい感じの色でお願いします。くすんだ色・ぼやけた色は好みではありません。
納品ファイル
• 高解像度JPG (.jpg)
• イラストレーター形式 (.ai)
補足説明
必ず入れてほしい項目は以下の通りです。

・サイト名(ひまわりルーム案内所)
※ロゴはそのまま使ってもかまいませんが、ロゴを使わずに色も形も変えてもかまいません。
ランディングページにあったロゴ(フォント)がベストです。(現在のロゴの色や形にこだわっていません)
・参加企業のパンフレット表紙
※実際に送るパンフがわかった方が、コンバージョンがよくなると思いますので..。
※参加企業は現在7社ですので、パンフも7点となります。ただし、今後は増減する可能性もありますので、7点に固執したデザインではなく、6点や8点になっても弊社で変更できるデザインを希望します。
・参加企業一覧とチェックボックス
※ランディングページ=資料請求ページになり、すぐに資料請求ができるようにします。
※現在の資料請求ページは以下の通りです。
http://www.rovino.net/rv/10.html
・トップページに戻るボタン
※ランディングページが孤立しないように、本来のサイトのトップに戻るボタンかテキストを入れてください。

なお、各社のパンフレットとリスティング広告に使用するバナーの見本は以下からDLしてご確認ください。
http://www.kz4.co.jp/pb.zip
納品ファイルに、イラストレーター形式 (.ai)を指定しましたが、イラストレーターがない場合は、jpgのみでもかまいません。
ただし、ご提案時に記載をしてください。
「イラストレーターがない場合は、jpgのみでもかまいません。」と追記しましたが、hmtl作成時にテキストが必要ですので、イラストレーターに替わるソフトがありましたら、記載していただけますよう、お願いいたします。(フォトショップやファイアーワークスなどです)
依頼途中で、サイトの参加会社が変わってしまったので、パンフレットを差し替えてアップしました。
同じURLですが、パンフを差し替えていますので、ご確認ください。
※既にダウンロード済みで、ご提案を製作中の場合は、古いパンフでも問題ありません。
(レイアウト確認だけですので..)
ただし、採用された場合は、最新のパンフレットで納品をお願いいたします。

インパクトには掛けますが、全体的な構成が整っていましたので、選ばせていただきました。

たくさんのご提案をいただき、ありがとうございました。
修正していただいた方はお手数をお掛けして、申し訳ございませんでした。
機会がございましたら、またよろしくお願いいたします。

```html
<!DOCTYPE html>
<html lang="ja">
<head>
<meta charset="utf-8">
<title>ひまわりルーム案内所 資料請求</title>
<link rel="stylesheet" href="https://fonts.googleapis.com/css2?family=M+PLUS+Rounded+1c:wght@500;800&family=Noto+Sans+JP:wght@400;700&display=swap">
<style>
:root{
  --green:#6cb33f;
  --green-dark:#3f8f1f;
  --green-pale:#eef7e3;
  --pink:#e8518a;
  --blue:#2a8fd6;
  --orange:#f39a1e;
  --orange-dark:#e0780b;
  --cork:#c99b63;
  --cork-dark:#b4834d;
  --ink:#333;
  --line:#c9dcb5;
  --white:#fff;
}
*{box-sizing:border-box;margin:0;padding:0}
html,body{width:857px;height:1200px;overflow:hidden}
body{font-family:"Noto Sans JP",sans-serif;color:var(--ink);background:var(--white);position:relative}
.topbar{position:absolute;left:0;top:0;width:857px;height:56px;background:var(--green);color:var(--white);
  font:800 24px "M PLUS Rounded 1c",sans-serif;display:flex;align-items:center;padding-left:28px;letter-spacing:1px}
.hero{position:absolute;left:0;top:56px;width:857px;height:372px;background:linear-gradient(#fff,var(--green-pale))}
.logo{position:absolute;left:22px;top:14px;font:800 40px "M PLUS Rounded 1c",sans-serif;color:var(--green-dark);display:flex;align-items:center;gap:10px}
.logo .dot{width:22px;height:22px;border-radius:50%;background:var(--orange)}
.hero-art{position:absolute;left:150px;top:78px;width:450px;height:290px;border-radius:8px;
  background:linear-gradient(135deg,#fbe4ee,#fdf6d8 55%,#d9efc4)}
.catch{position:absolute;right:24px;top:26px;text-align:center;font-family:"M PLUS Rounded 1c",sans-serif;font-weight:800}
.catch .l1{font-size:34px;color:#222}
.catch .l2{font-size:40px;color:#222}
.catch .l3{font-size:38px;color:#222;margin-top:4px}
.catch .tag{display:inline-block;background:var(--blue);color:#fff;padding:0 8px;border-radius:4px}
.catch .pink{color:var(--pink)}
.features{position:absolute;left:0;top:428px;width:857px;height:398px}
.girl-art{position:absolute;left:16px;top:40px;width:120px;height:340px;border-radius:60px 60px 10px 10px;background:linear-gradient(#f7d3e2,#f3b9cf)}
.board{position:absolute;left:140px;top:10px;width:420px;height:380px;background:var(--cork);border:8px solid var(--cork-dark);border-radius:6px}
.board-title{position:absolute;left:20px;top:22px;background:var(--green);color:#fff;font:800 22px "M PLUS Rounded 1c",sans-serif;padding:6px 18px;border-radius:4px}
.note{position:absolute;font-size:13px;line-height:1.5;padding:10px 12px;box-shadow:2px 3px 4px rgba(0,0,0,.25);color:#333}
.note.y{background:#fff7b0}.note.w{background:#fff}.note.p{background:#ffd9e6}.note.g{background:#dff2c8}
.pamphlets{position:absolute;left:576px;top:20px;width:262px;display:grid;grid-template-columns:1fr 1fr;gap:10px}
.cover{height:84px;border:1px solid #ddd;box-shadow:1px 2px 3px rgba(0,0,0,.2)}
.request{position:absolute;left:0;top:832px;width:857px;height:290px}
.company-table{position:absolute;left:24px;top:0;width:530px;border-collapse:collapse;font-size:12px}
.company-table th{background:var(--green);color:#fff;padding:6px;font-weight:700;text-align:left}
.company-table td{border-bottom:1px solid var(--line);padding:5px 6px;height:29px}
.company-table tr:nth-child(even) td{background:var(--green-pale)}
.check{width:14px;height:14px;border:1.5px solid #888;background:#fff;display:inline-block;vertical-align:middle}
.cta{position:absolute;left:578px;top:0;width:258px}
.cta h2{font:800 24px "M PLUS Rounded 1c",sans-serif;color:var(--green-dark);border-bottom:3px solid var(--green);padding-bottom:6px}
.cta p{font-size:12px;line-height:1.7;margin-top:12px}
.cta p em{color:var(--pink);font-style:normal;font-weight:700}
.btn-request{margin-top:22px;height:72px;border-radius:8px;background:linear-gradient(#fbb34a,var(--orange-dark));
  color:#fff;font:800 26px "M PLUS Rounded 1c",sans-serif;display:flex;align-items:center;justify-content:center;gap:10px;box-shadow:0 3px 0 #b85f05}
.footer{position:absolute;left:0;top:1132px;width:857px;height:68px;background:var(--green);display:flex;align-items:center;justify-content:space-between;padding:0 28px}
.footer p{color:#fff;font:800 20px "M PLUS Rounded 1c",sans-serif}
.btn-top{background:#fff;color:var(--green-dark);font-weight:700;font-size:14px;padding:8px 18px;border-radius:4px;display:flex;align-items:center;gap:6px}
</style>
</head>
<body>
<header class="topbar">これから一人暮らしをお考えの学生の方へ　おすすめ物件</header>

<section class="hero">
  <div class="logo"><span class="dot"></span>ひまわりルーム案内所</div>
  <div class="hero-art" role="img" aria-label="明るい部屋でくつろぐ女子学生のイラスト"></div>
  <div class="catch">
    <div class="l1">学生マンションなら</div>
    <div class="l2">24時間いつでも</div>
    <div class="l3"><span class="tag">安心</span>で<span class="pink">快適</span>ライフ</div>
  </div>
</section>

<section class="features">
  <div class="girl-art" role="img" aria-label="立っている女子学生のイラスト"></div>
  <div class="board" role="img" aria-label="コルクボード">
    <div class="board-title">学生マンションの特徴</div>
    <div class="note w" style="left:200px;top:70px;width:180px">心豊かで安全な<br>キャンパスライフを<br>過ごすために。</div>
    <div class="note y" style="left:24px;top:110px;width:150px">オートロックで<br>女性の一人暮らしも<br>安心です。</div>
    <div class="note p" style="left:210px;top:170px;width:170px">家具・家電付きで<br>すぐに新生活を<br>始められます。</div>
    <div class="note g" style="left:30px;top:210px;width:160px">管理人が常駐して<br>いるので困った時も<br>すぐ相談できます。</div>
    <div class="note w" style="left:24px;top:296px;width:170px">「学生ならでは」の<br>サポートが充実！</div>
    <div class="note y" style="left:230px;top:270px;width:140px">学校や駅の近くの<br>物件も多数！</div>
  </div>
  <div class="pamphlets">
    <div class="cover" role="img" aria-label="参加企業パンフレット表紙" style="background:linear-gradient(#f9e79a,#f4c24a)"></div>
    <div class="cover" role="img" aria-label="参加企業パンフレット表紙" style="background:linear-gradient(#fbd0de,#ef8fb1)"></div>
    <div class="cover" role="img" aria-label="参加企業パンフレット表紙" style="background:linear-gradient(#cfe8fb,#7fbde8)"></div>
    <div class="cover" role="img" aria-label="参加企業パンフレット表紙" style="background:linear-gradient(#e5f3d4,#9fd06b)"></div>
    <div class="cover" role="img" aria-label="参加企業パンフレット表紙" style="background:linear-gradient(#fde0c4,#f5a25a)"></div>
    <div class="cover" role="img" aria-label="参加企業パンフレット表紙" style="background:linear-gradient(#f3d9f1,#d08cc9)"></div>
    <div class="cover" role="img" aria-label="参加企業パンフレット表紙" style="background:linear-gradient(#dff4f4,#7ccfcf)"></div>
    <div class="cover" role="img" aria-label="参加企業パンフレット表紙" style="background:linear-gradient(#fff,#f1e3ea)"></div>
  </div>
</section>

<section class="request">
  <table class="company-table">
    <tr><th style="width:40px">選択</th><th>会社名</th><th>対応エリア</th></tr>
    <tr><td><span class="check"></span></td><td>株式会社ひだまり住宅</td><td>東京・神奈川・埼玉</td></tr>
    <tr><td><span class="check"></span></td><td>そよかぜレジデンス</td><td>京都・大阪・兵庫</td></tr>
    <tr><td><span class="check"></span></td><td>学生ハウス協同会</td><td>東京・千葉・埼玉</td></tr>
    <tr><td><span class="check"></span></td><td>みどり学生寮株式会社</td><td>愛知・岐阜・三重</td></tr>
    <tr><td><span class="check"></span></td><td>あおば不動産</td><td>福岡・熊本</td></tr>
    <tr><td><span class="check"></span></td><td>キャンパスホーム株式会社</td><td>全国主要都市</td></tr>
    <tr><td><span class="check"></span></td><td>こもれび住まい</td><td>北海道・宮城</td></tr>
  </table>
  <div class="cta">
    <h2>まずは資料請求から！</h2>
    <p>気になる会社にチェックを入れて、ボタンを押すだけで<em>資料がまとめて届きます。</em>もちろん資料請求は無料です。お部屋探しの第一歩にぜひご活用ください。</p>
    <div class="btn-request">
      <svg width="26" height="26" viewBox="0 0 26 26" aria-hidden="true"><circle cx="13" cy="13" r="12" fill="#fff"/><path d="M10 7l7 6-7 6" fill="none" stroke="#e0780b" stroke-width="3"/></svg>
      一括資料請求
    </div>
  </div>
</section>

<footer class="footer">
  <p>学生マンションについてもっと詳しく知りたい方は</p>
  <div class="btn-top">
    <svg width="14" height="14" viewBox="0 0 14 14" aria-hidden="true"><path d="M4 2l6 5-6 5" fill="none" stroke="#3f8f1f" stroke-width="2.5"/></svg>
    サイトのトップページへ
  </div>
</footer>
</body>
</html>
```